Business Card Design for Consulting Company

I require a Business Card design for my Consulting company. <br/><br/>My company name is: Marek Olvani Consulting Inc.<br/>My website is: www.marekolvaniconsulting.example<br/><br/>My company focuses on management and software development for the Tallobrix CRM platform (www.tallobrix.example)<br/><br/>I have a logo already designed...see attached.
Updates

Also Include my Name and Title: Marek T.L. Olvani President

Target Market(s)

Tallobrix Customers

Contact Information for Business Card

Only include my LOGO (provided)
My Name: Marek TL Olvani
My Title: President
My Company Name: Marek Olvani Consulting Inc.
My Website: www.marekolvaniconsulting.example
My Email: marek.olvani.consulting@mailbox.example

NO PHONE NUMBER
NO ADDRESS

Font styles to use
Serif
Sans Serif
Other font styles liked:
• see my website: www.marekolvaniconsulting.example

Colors

Designer to choose colors to be used in the design.

Requirements
Must have
• Must include my Orange
• Include my name (Marek T.L. Olvani), title (President) company name, website and email
• It should also have a tag line like: Tallobrix Consulting
• I'm flexible with the tag line
Should not have
• Don't include my phone number or address

```html
<!DOCTYPE html>
<html lang="en">
<head>
<meta charset="utf-8">
<title>Marek Olvani Consulting Inc. – Business Card</title>
<link href="https://fonts.googleapis.com/css2?family=Exo+2:wght@500&family=Open+Sans:wght@400;600&display=swap" rel="stylesheet">
<style>
  :root {
    --backdrop: #dcdbd7;
    --card: #2e2e30;
    --card-deep: #29292b;
    --orange: #f7861d;
    --ink-light: #e9e9e9;
    --ink-muted: #bdbdbd;
    --mark-faint: #3a3a3d;
  }
  * { box-sizing: border-box; margin: 0; padding: 0; }
  html, body { width: 1200px; height: 801px; overflow: hidden; }
  body {
    background: var(--backdrop);
    font-family: "Open Sans", sans-serif;
    position: relative;
  }
  .card {
    position: absolute;
    top: 249px;
    width: 530px;
    height: 303px;
    background: var(--card);
    border-bottom: 3px solid var(--orange);
    overflow: hidden;
  }
  .card--front { left: 50px; }
  .card--back { left: 620px; background: var(--card-deep); }

  .brand {
    position: absolute;
    display: flex;
    align-items: center;
    gap: 8px;
    font-family: "Exo 2", sans-serif;
    font-weight: 500;
  }
  .brand__square { background: var(--orange); }
  .brand__name { color: var(--orange); }

  .card--front .brand { left: 34px; top: 126px; }
  .card--front .brand__square { width: 12px; height: 12px; }
  .card--front .brand__name { font-size: 26px; letter-spacing: 0.5px; }

  .company-name {
    position: absolute;
    left: 210px;
    top: 56px;
    font-family: "Exo 2", sans-serif;
    font-weight: 500;
    font-size: 24px;
    line-height: 27px;
    letter-spacing: 0.6px;
    text-transform: uppercase;
    color: var(--orange);
  }
  .divider {
    position: absolute;
    left: 212px;
    right: 0;
    top: 122px;
    height: 1.5px;
    background: var(--orange);
  }
  .person {
    position: absolute;
    left: 212px;
    top: 136px;
    color: var(--ink-light);
  }
  .person__name {
    font-size: 14px;
    font-weight: 600;
    line-height: 20px;
  }
  .person__title {
    font-size: 12px;
    line-height: 17px;
    color: var(--ink-muted);
  }
  .contact {
    position: absolute;
    left: 212px;
    top: 184px;
    list-style: none;
    font-size: 12.5px;
    line-height: 18px;
    color: var(--ink-light);
  }
  .tagline {
    position: absolute;
    left: 212px;
    top: 248px;
    font-family: "Exo 2", sans-serif;
    font-weight: 500;
    font-size: 15px;
    letter-spacing: 1.2px;
    color: var(--orange);
  }

  .card--back .brand {
    left: 50%;
    top: 50%;
    transform: translate(-50%, -50%);
    gap: 14px;
  }
  .card--back .brand__square { width: 22px; height: 22px; background: var(--mark-faint); }
  .card--back .brand__name { font-size: 60px; color: var(--mark-faint); }
</style>
</head>
<body>
  <section class="card card--front" aria-label="Business card front">
    <div class="brand">
      <span class="brand__square"></span>
      <span class="brand__name">Olvani</span>
    </div>
    <h1 class="company-name">Marek Olvani<br>Consulting Inc.</h1>
    <div class="divider"></div>
    <div class="person">
      <p class="person__name">Marek T.L. Olvani</p>
      <p class="person__title">President</p>
    </div>
    <ul class="contact">
      <li>marek.olvani.consulting@mailbox.example</li>
      <li>www.marekolvaniconsulting.example</li>
    </ul>
    <p class="tagline">Tallobrix Consulting</p>
  </section>

  <section class="card card--back" aria-label="Business card back">
    <div class="brand">
      <span class="brand__square"></span>
      <span class="brand__name">Olvani</span>
    </div>
  </section>
</body>
</html>
```